Genetics Lab Testing Flyers

I have 5 flyers for another laboratory that I will be working with that need to have the logos and colors changed to match our laboratory, all of the information is correct its just changing of the format, logo and color scheme. I have attached 2 versions of our logo as well. (silver birch labs)

Target Market(s)

physician offices

Industry/Entity Type

Healthcare - Laboratoy

Colors
0054AA
0677BA
7BADD7
CADEEF
E8F1F8

Requirements
Must have
• all the information on the 5 current flyers
Should not have
• any mention of TraxoKey

```html
<!DOCTYPE html>
<html lang="en">
<head>
<meta charset="utf-8">
<title>Government Initiative – Cancer Prevention and Early Detection</title>
<link rel="stylesheet" href="https://fonts.googleapis.com/css2?family=Montserrat:wght@600;700;800&family=Lato:wght@400;700&display=swap">
<style>
  :root {
    --blue: #1f74bf;
    --blue-dark: #0054aa;
    --blue-pale: #eaf4fb;
    --ink: #1e1e1e;
    --text: #4a4a4a;
    --heading: #555657;
    --footer: #59595b;
    --white: #ffffff;
  }
  html, body { margin: 0; padding: 0; overflow: hidden; background: var(--white); }
  .flyer {
    position: relative; width: 927px; height: 1200px; overflow: hidden;
    font-family: 'Lato', sans-serif; color: var(--text); background: var(--white);
  }
  .brand { position: absolute; display: flex; align-items: center; gap: 8px; }
  .brand-dot { width: 16px; height: 16px; border-radius: 50%; background: var(--blue); flex: none; }
  .brand-name {
    font-family: 'Montserrat', sans-serif; font-weight: 700; color: var(--blue);
    font-size: 19px; letter-spacing: 0.5px; white-space: nowrap;
  }
  .header-brand { left: 37px; top: 52px; }
  .title {
    position: absolute; left: 362px; top: 16px; margin: 0;
    font-family: 'Montserrat', sans-serif; font-weight: 800; font-size: 38px;
    color: var(--blue); letter-spacing: 0.2px; white-space: nowrap;
  }
  .subtitle {
    position: absolute; left: 363px; top: 70px; width: 540px; margin: 0;
    font-size: 15px; line-height: 22px; color: var(--ink); letter-spacing: -0.1px;
  }
  .update-band {
    position: absolute; left: 0; top: 128px; width: 927px; height: 37px;
    background: var(--blue); color: var(--white); font-weight: 700; font-size: 15.5px;
    display: flex; align-items: center; padding-left: 37px; box-sizing: border-box; white-space: nowrap;
  }
  .purpose {
    position: absolute; left: 0; top: 165px; width: 927px; height: 149px; background: var(--blue-pale);
  }
  .purpose-label {
    position: absolute; left: 37px; top: 18px; margin: 0;
    font-weight: 700; font-size: 19px; color: var(--ink);
  }
  .purpose-text {
    position: absolute; left: 138px; top: 15px; width: 757px; margin: 0;
    font-size: 16px; line-height: 29px; color: var(--ink); text-align: justify; letter-spacing: -0.25px;
  }
  .banner {
    position: absolute; left: 86px; top: 333px; width: 805px; height: 104px;
    background: var(--blue); border-radius: 0 52px 52px 0;
  }
  .banner-badge {
    position: absolute; left: 34px; top: 333px; width: 102px; height: 102px; border-radius: 50%;
    background: var(--white); border: 1px solid #e3e3e3;
  }
  .banner-title {
    position: absolute; left: 168px; top: 343px; margin: 0;
    font-family: 'Montserrat', sans-serif; font-weight: 700; font-size: 31px; line-height: 40px; color: var(--white);
  }
  .section-heading {
    position: absolute; margin: 0; font-family: 'Montserrat', sans-serif; font-weight: 700;
    font-size: 21px; color: var(--heading); padding-bottom: 9px;
  }
  .section-heading::after {
    content: ""; position: absolute; left: 0; bottom: 0; width: 69px; height: 2px; background: var(--blue);
  }
  .points { position: absolute; margin: 0; padding: 0; list-style: none; }
  .points li {
    position: relative; padding-left: 30px; font-size: 14.5px; line-height: 22px;
    text-align: justify; margin-bottom: 5px; letter-spacing: -0.15px;
  }
  .points li svg { position: absolute; left: 1px; top: 5px; }
  .problem-heading { left: 37px; top: 463px; }
  .problem-list { left: 37px; top: 516px; width: 389px; }
  .plan-heading { left: 502px; top: 463px; }
  .plan-list { left: 502px; top: 516px; width: 389px; }
  .plan-list li.gap { margin-top: 10px; }
  .you-heading { left: 502px; top: 889px; }
  .you-list { left: 502px; top: 942px; width: 389px; }
  .lab-photo {
    position: absolute; left: 37px; top: 773px; width: 426px; height: 295px; border-radius: 22px;
    background: linear-gradient(135deg, #0f3f6e 0%, #2d7bb8 45%, #9fd0ee 75%, #d9ecf8 100%);
  }
  .footer {
    position: absolute; left: 0; top: 1089px; width: 927px; height: 111px; background: var(--footer); color: var(--white);
  }
  .contact { position: absolute; font-size: 15px; line-height: 25px; }
  .contact-row { display: flex; align-items: center; gap: 12px; height: 25px; }
  .contact-row .icon { width: 20px; display: flex; justify-content: center; }
  .phones { left: 37px; top: 14px; }
  .place { left: 686px; top: 12px; }
  .footer-brand { left: 371px; top: 44px; }
  .footer-brand .brand-name { color: var(--white); font-size: 21px; }
  .footer-brand .brand-dot { background: var(--white); }
</style>
</head>
<body>
<div class="flyer">

  <div class="brand header-brand"><span class="brand-dot"></span><span class="brand-name">SILVER BIRCH LABS</span></div>

  <h1 class="title">GOVERNMENT INITIATIVE</h1>
  <p class="subtitle">to “End Cancer as We Know It” (Cancer Moonshot) Releases Report with Strong Support for Genetic Testing</p>

  <div class="update-band">Update: On December 7th, 2016 Congress passed a bill, dedicating $1.8 billion in funding over 10 years for the Moonshot</div>

  <section class="purpose">
    <h2 class="purpose-label">Purpose:</h2>
    <p class="purpose-text">The “Cancer Moonshot” was announced by President Daniel Harlow in his State of the Union addres on January 12, 2016. Led by Vice President Thomas Reed, the initiative is tasked with ending cancer as we know it, and doubling the rate of progress towards a cure. On September 7th, 2016 they released a statement with specific recommendations.</p>
  </section>

  <div class="banner"></div>
  <div class="banner-badge"></div>
  <h2 class="banner-title">Cancer Prevention and Early Detection<br>in Individuals at High Risk for Cancer</h2>

  <svg width="0" height="0" style="position:absolute">
    <symbol id="arrow-bullet" viewBox="0 0 14 14">
      <circle cx="7" cy="7" r="7" fill="#1f74bf"/>
      <path d="M3.6 7h6M7.4 4.6 9.8 7l-2.4 2.4" stroke="#fff" stroke-width="1.5" fill="none" stroke-linecap="round" stroke-linejoin="round"/>
    </symbol>
  </svg>

  <h3 class="section-heading problem-heading">The Problem:</h3>
  <ul class="points problem-list">
    <li><svg width="13" height="13"><use href="#arrow-bullet"/></svg>“It is estimated that more than half of all cancer deaths could be prevented”</li>
    <li><svg width="13" height="13"><use href="#arrow-bullet"/></svg>“Underuse of germline (hereditary) cancer testing in appropriate populations is leading to unnecessarily lost lives and diminished</li>
    <li><svg width="13" height="13"><use href="#arrow-bullet"/></svg>12 million people are living with BRCA and Lynch Syndrome mutations</li>
    <li><svg width="13" height="13"><use href="#arrow-bullet"/></svg>Less than 1.2% of people with Lynch Syndrome are aware of their status. Similarly, only a small percentage of BRCA mutation carriers know their status</li>
  </ul>

  <div class="lab-photo" role="img" aria-label="Photo of a laboratory scientist in a white coat and safety glasses working at a microscope among glassware"></div>

  <h3 class="section-heading plan-heading">The Plan:</h3>
  <ul class="points plan-list">
    <li><svg width="13" height="13"><use href="#arrow-bullet"/></svg>Develop effective strategies to scale up HBOC and LS screening and deliver evidencebased</li>
    <li><svg width="13" height="13"><use href="#arrow-bullet"/></svg>Better insurance coverage for testing, particularly among poor and minority groups (with specific mention of Medicaid)</li>
    <li><svg width="13" height="13"><use href="#arrow-bullet"/></svg>Education of primary care providers to increase use of appropriate screening, counseling and evidencebased genetic tests</li>
    <li><svg width="13" height="13"><use href="#arrow-bullet"/></svg>Use of Next-Generation Sequencing to look at genes beyond just BRCA1, BRCA2 and the Lynch Syndrome genes</li>
    <li class="gap"><svg width="13" height="13"><use href="#arrow-bullet"/></svg>Better general education so more people are aware of the genetics of cancer risk</li>
    <li class="gap"><svg width="13" height="13"><use href="#arrow-bullet"/></svg>Testing of germline DNA for cancer patients along with testing their tumor</li>
  </ul>

  <h3 class="section-heading you-heading">What this means for you:</h3>
  <ul class="points you-list">
    <li><svg width="13" height="13"><use href="#arrow-bullet"/></svg>The government is putting its weight behind cancer risk predisposition testing because of the proven benefits of such testing for your patients. As Medicare and other insurances shift from feeforservice to qualityand valuebased payments, a focus on prevention should also benefit the practice as well.</li>
  </ul>

  <footer class="footer">
    <div class="contact phones">
      <div class="contact-row"><span class="icon"><svg width="18" height="18" viewBox="0 0 24 24"><path d="M6.6 10.8a15 15 0 0 0 6.6 6.6l2.2-2.2a1 1 0 0 1 1-.25 11.4 11.4 0 0 0 3.6.57 1 1 0 0 1 1 1V20a1 1 0 0 1-1 1A17 17 0 0 1 3 4a1 1 0 0 1 1-1h3.5a1 1 0 0 1 1 1c0 1.250.2 2.450.57 3.6a1 1 0 0 1-.25 1z" fill="#fff"/></svg></span>(877) GENE-KEY</div>
      <div class="contact-row"><span class="icon"></span>(555) 310-0186</div>
      <div class="contact-row"><span class="icon"><svg width="16" height="16" viewBox="0 0 16 16"><rect x="1" y="5" width="14" height="10" rx="1" fill="none" stroke="#fff" stroke-width="1.4"/><rect x="4" y="1" width="8" height="5" fill="none" stroke="#fff" stroke-width="1.4"/><path d="M4 9h2M7 9h2M10 9h2M4 12h2M7 12h2M10 12h2" stroke="#fff" stroke-width="1.3"/></svg></span>(555) 310-0191</div>
    </div>

    <div class="brand footer-brand"><span class="brand-dot"></span><span class="brand-name">SILVER BIRCH LABS</span></div>

    <div class="contact place">
      <div class="contact-row"><span class="icon"><svg width="14" height="18" viewBox="0 0 14 18"><path d="M7 0a7 7 0 0 0-7 7c0 5 7 11 7 11s7-6 7-11a7 7 0 0 0-7-7zm0 9.6A2.6 2.6 0 1 1 7 4.4a2.6 2.6 0 0 1 0 5.2z" fill="#fff"/></svg></span>48 Linden Park Rd.</div>
      <div class="contact-row"><span class="icon"></span>Fairhaven, NJ 07710 U.S.A.</div>
      <div class="contact-row"><span class="icon"><svg width="18" height="13" viewBox="0 0 18 13"><rect x="0.7" y="0.7" width="16.6" height="11.6" fill="none" stroke="#fff" stroke-width="1.4"/><path d="M1 1l8 6.5L17 1M1 12l6-5M17 12l-6-5" stroke="#fff" stroke-width="1.3" fill="none"/></svg></span>info@SilverBirchLab.com</div>
    </div>
  </footer>

</div>
</body>
</html>
```